Looking for awesome business card design with attached existing logo

We are a water, mold, and fire damage restoration company called "Torvane Seco" Looking for an awesome business card that is edgy yet professional and unique. Show me what you got!

```html
<!DOCTYPE html>
<html lang="en">
<head>
<meta charset="utf-8">
<title>Torvane Seco — Business Card</title>
<link href="https://fonts.googleapis.com/css2?family=Montserrat:wght@600;700&family=Arimo:wght@400;700&display=swap" rel="stylesheet">
<style>
  :root {
    --slate: #2c4a57;
    --gold: #d9981f;
    --paper: #ffffff;
    --backdrop: #e4e4e4;
    --ink-light: #ffffff;
  }
  html, body {
    margin: 0;
    padding: 0;
    width: 1200px;
    height: 1020px;
    overflow: hidden;
    background: var(--backdrop);
  }
  .canvas {
    position: relative;
    width: 1200px;
    height: 1020px;
  }
  .card {
    position: absolute;
    left: 200px;
    width: 800px;
    height: 457px;
    background: var(--paper);
    box-shadow: 0 4px 14px rgba(0,0,0,0.12);
    overflow: hidden;
  }
  .card-front { top: 40px; }
  .card-back  { top: 530px; display: flex; }

  .wordmark {
    font-family: "Montserrat", sans-serif;
    font-weight: 700;
    color: var(--slate);
    letter-spacing: 1px;
    display: flex;
    align-items: center;
    gap: 14px;
    white-space: nowrap;
  }
  .wordmark-dot {
    display: inline-block;
    border-radius: 50%;
    background: var(--gold);
  }

  .card-front .wordmark {
    position: absolute;
    top: 150px;
    left: 0;
    right: 0;
    justify-content: center;
    font-size: 58px;
  }
  .card-front .wordmark-dot { width: 30px; height: 30px; }
  .front-url {
    position: absolute;
    bottom: 70px;
    left: 0;
    right: 0;
    text-align: center;
    font-family: "Arimo", sans-serif;
    font-weight: 700;
    font-size: 19px;
    letter-spacing: 1px;
    color: var(--slate);
  }

  .back-brand {
    width: 44%;
    display: flex;
    align-items: center;
    justify-content: center;
  }
  .back-brand .wordmark { font-size: 34px; gap: 10px; }
  .back-brand .wordmark-dot { width: 18px; height: 18px; }

  .back-details {
    width: 56%;
    background: var(--slate);
    color: var(--ink-light);
    font-family: "Arimo", sans-serif;
    padding: 62px 40px 0 56px;
    box-sizing: border-box;
    position: relative;
  }
  .holder-name {
    font-weight: 700;
    font-size: 32px;
    color: var(--gold);
    margin: 0;
    line-height: 1.05;
  }
  .holder-title {
    font-size: 16px;
    text-transform: uppercase;
    letter-spacing: 0.5px;
    margin: 2px 0 30px;
  }
  .contact-row {
    display: flex;
    justify-content: space-between;
    align-items: flex-start;
    margin-bottom: 24px;
  }
  .contact-lines {
    font-size: 25px;
    line-height: 1.1;
  }
  .contact-icon {
    width: 34px;
    height: 34px;
    flex: none;
  }
</style>
</head>
<body>
<main class="canvas">

  <section class="card card-front" aria-label="Card front">
    <div class="wordmark"><span class="wordmark-dot"></span>Torvane Seco</div>
    <div class="front-url">WWW.TORVANESECO.COM</div>
  </section>

  <section class="card card-back" aria-label="Card back">
    <div class="back-brand">
      <div class="wordmark"><span class="wordmark-dot"></span>Torvane Seco</div>
    </div>
    <div class="back-details">
      <p class="holder-name">Marta Quill</p>
      <div class="holder-title">General Manager</div>

      <div class="contact-row">
        <div class="contact-lines">555.318-4620<br>800-555-0199</div>
        <svg class="contact-icon" viewBox="0 0 34 34" aria-hidden="true">
          <circle cx="17" cy="17" r="17" fill="var(--gold)"/>
          <path d="M11 10c1-1 2-1 3 0l2 3c.5 1 0 2-1 2.5 1 2 2.5 3.5 4.5 4.5.5-1 1.5-1.5 2.5-1l3 2c1 1 1 2 0 3-2 2-5 1.5-8-1s-5-5-7-8c-1.5-2-1-3.5 1-5z" fill="var(--slate)"/>
        </svg>
      </div>

      <div class="contact-row">
        <div class="contact-lines">48 harbor lane<br>city, state 04721</div>
        <svg class="contact-icon" viewBox="0 0 34 34" aria-hidden="true">
          <circle cx="17" cy="17" r="17" fill="var(--gold)"/>
          <path d="M17 7a7 7 0 0 0-7 7c0 5 7 13 7 13s7-8 7-13a7 7 0 0 0-7-7z" fill="var(--slate)"/>
          <circle cx="17" cy="14" r="2.8" fill="var(--gold)"/>
        </svg>
      </div>

      <div class="contact-row">
        <div class="contact-lines">www.torvaneseco.com<br>mquill@torvaneseco.com</div>
        <svg class="contact-icon" viewBox="0 0 34 34" aria-hidden="true">
          <circle cx="17" cy="17" r="17" fill="var(--gold)"/>
          <g fill="none" stroke="var(--slate)" stroke-width="1.8">
            <circle cx="17" cy="17" r="9"/>
            <ellipse cx="17" cy="17" rx="4" ry="9"/>
            <line x1="8" y1="17" x2="26" y2="17"/>
            <line x1="9.5" y1="12.5" x2="24.5" y2="12.5"/>
            <line x1="9.5" y1="21.5" x2="24.5" y2="21.5"/>
          </g>
        </svg>
      </div>
    </div>
  </section>

</main>
</body>
</html>
```